Marlowick APP redesign and color change

I am looking for a new design for my app. Please see the attached current design.

Currently, I have a functioning app but the colors and design are awful!
The logo is great but the rest of the app needs a refresh.
(Logo hi res not yet available but will upload soon.)
New colors or anything that is cutting edge.

Basically: It is a secure social media app within a school system where the teachers, students and parents can text, exchange photos, plan curriculum, etc.

I NEED ONLY landing page with a new look!
Looking for one distinct design for the landing page with new look.
The developer will apply this one design towards the rest of the pages/app screens.

Because part of the social media I need the feel and look of what is now the trend. Something that will attract and keep the client(s) interested. I am really leaving all the creative work to the designer and open to any suggestions.
Updates

Target Market(s)

Schools, community, teachers, students, colleges, sport teams

Industry/Entity Type

Non Profit

Font styles to use
Serif
Sans Serif

Colors

Designer to choose colors to be used in the design.

Requirements
Must have
• Sharp, trendy, millennial feel
Nice to have
• Up to designer
Should not have
• Up to designer

```html
<!DOCTYPE html>
<html lang="en">
<head>
<meta charset="UTF-8">
<title>Marlowick — Sign In</title>
<link rel="stylesheet" href="https://fonts.googleapis.com/css2?family=Lato:wght@400;700&family=Roboto:wght@400&display=swap">
<style>
  :root {
    --olive-dark: #2a2c12;
    --olive-mid: #5b5a2a;
    --olive-warm: #8a7a3c;
    --field-green-top: #2c3a08;
    --field-green-bottom: #5a6b0c;
    --gold: #b87c00;
    --card-white: rgba(255, 255, 255, 0.9);
    --ink: #2b2b2b;
    --rule: #6a6a6a;
    --white: #ffffff;
    --soft-white: #f1f1e6;
  }
  * { box-sizing: border-box; margin: 0; padding: 0; }
  html, body { width: 741px; height: 1200px; overflow: hidden; }
  body {
    position: relative;
    font-family: "Lato", sans-serif;
    background: linear-gradient(180deg, var(--field-green-top) 0%, var(--field-green-bottom) 100%);
  }
  .hero-photo {
    position: absolute;
    left: 0; top: 0;
    width: 741px; height: 1023px;
    background:
      linear-gradient(180deg, #4a4a30 0%, #4a4a30 8%, #7a5a34 8.2%, #7a5a34 9.6%, var(--olive-dark) 10%, var(--olive-mid) 45%, var(--olive-warm) 75%, #a59a70 100%);
  }
  .brand {
    position: absolute;
    left: 0; top: 405px;
    width: 741px;
    display: flex;
    justify-content: center;
    align-items: center;
    gap: 16px;
  }
  .brand-mark {
    width: 22px; height: 22px;
    border-radius: 50%;
    background: var(--white);
  }
  .brand-name {
    font-family: "Lato", sans-serif;
    font-weight: 700;
    font-size: 33px;
    letter-spacing: 17px;
    color: var(--white);
  }
  .login-card {
    position: absolute;
    left: 93px; top: 653px;
    width: 556px; height: 317px;
    background: var(--card-white);
    padding: 62px 62px 0 62px;
  }
  .field-label {
    display: block;
    font-size: 15.5px;
    letter-spacing: 1.6px;
    color: var(--gold);
    text-transform: uppercase;
  }
  .field-value {
    font-family: "Roboto", sans-serif;
    font-size: 23px;
    color: var(--ink);
    margin-top: 11px;
    padding-bottom: 16px;
    border-bottom: 1.5px solid var(--rule);
  }
  .field-password { margin-top: 34px; }
  .password-dots {
    display: flex;
    gap: 9.5px;
    margin-top: 30px;
  }
  .password-dots span {
    width: 8px; height: 8px;
    border-radius: 50%;
    background: var(--ink);
  }
  .get-started {
    position: absolute;
    left: 93px; top: 970px;
    width: 556px; height: 106px;
    background: var(--gold);
    display: flex;
    align-items: center;
    justify-content: space-between;
    padding: 0 57px 0 62px;
    color: var(--white);
    font-size: 23px;
  }
  .register-link {
    position: absolute;
    left: 0; top: 1119px;
    width: 741px;
    text-align: center;
    font-size: 18px;
    color: var(--soft-white);
  }
</style>
</head>
<body>
  <div class="hero-photo" role="img" aria-label="Photo of two smiling students at a desk in front of a chalkboard, with an olive tint"></div>

  <div class="brand">
    <span class="brand-mark"></span>
    <span class="brand-name">MARLOWICK</span>
  </div>

  <form class="login-card">
    <label class="field-label">Username</label>
    <div class="field-value">todd@learnhub.net</div>
    <div class="field-password">
      <label class="field-label">Password</label>
      <div class="password-dots" aria-label="Password hidden">
        <span></span><span></span><span></span><span></span><span></span><span></span><span></span><span></span>
      </div>
    </div>
  </form>

  <div class="get-started">
    <span>Get Started</span>
    <svg width="14" height="18" viewBox="0 0 14 18" aria-hidden="true"><path d="M0 0 L14 9 L0 18 Z" fill="#111"/></svg>
  </div>

  <p class="register-link">Not registered? Create Account</p>
</body>
</html>
```